Full Service Outdoor Property Management Company

We are looking for a new and fresh business card design. My company has been in business for 26 years. Winter: We are a large snow and ice management company that does work for commercial, industrial and municipal clients. We have been named "Top 100 Snow Companies in the U.S." for numerous years. Summer: We provide complete landscape maintenance and landscape design and construction for both residential and commercial clients. We must incorporate our logo into card design as well as (in no particular order):
Employees name
Office: (417) 803-2765
Cell: (xxx) xxx-xxxx
brightfold.com
1879 Marigold, Larkmont OH 43917
(Something about 26 + years in business as well as "Top 100 snow contractors as stated above)
Target Market(s)
Winter: Commercial, Industrial, Municipal
Summer: Residential and Commercial
Industry/Entity Type
Construction
Contact Information for Business Card
This is a little challenging as we are using one card for essentially two companies that target different customers from summer to winter. Perhaps the back side could be split in two or something to highlight the different services?? I'm open to any ideas!! Looking forward to seeing what you come up with!
Requirements
Must have
- Logo
- (in no particular order)
- Employees name
- Office: (417) 803-2765
- Cell: (xxx) xxx-xxxx
- brightfold.com
- 1879 Marigold, Larkmont OH 43917
Nice to have
- Something about 26 + years in business
- "Top 100 Snow Contractors in the U.S."
Should not have
- Cheesy pictures of lawn mowers and snow plows

```html
<!DOCTYPE html>
<html lang="en">
<head>
<meta charset="utf-8">
<title>Brightfold Business Card</title>
<link rel="stylesheet" href="https://fonts.googleapis.com/css2?family=Open+Sans:wght@400;600;700&display=swap">
<style>
  :root {
    --backdrop: #d9dbdc;
    --brand-green: #0f7a45;
    --accent-blue: #3a86c8;
    --ink: #3a3a3a;
    --paper: #ffffff;
    --divider: #b9b9b9;
  }
  * { box-sizing: border-box; margin: 0; padding: 0; }
  html, body {
    width: 1200px; height: 960px; overflow: hidden;
    background: var(--backdrop);
    font-family: "Open Sans", Arial, sans-serif;
  }
  .card {
    position: absolute; left: 220px; width: 760px; height: 434px;
    border-radius: 26px; overflow: hidden;
    box-shadow: 0 6px 18px rgba(0,0,0,0.18);
  }
  .card--back { top: 30px; background: var(--brand-green); color: var(--paper); }
  .card--front { top: 496px; background: var(--paper); color: var(--ink); }

  .wordmark {
    position: absolute; left: 0; right: 0;
    font-weight: 600; letter-spacing: 1px; line-height: 1;
    display: flex; justify-content: center; align-items: center; gap: 14px;
  }
  .wordmark__dot { width: 18px; height: 18px; border-radius: 50%; }
  .card--back .wordmark { top: 48px; font-size: 50px; color: var(--paper); }
  .card--back .wordmark__dot { background: var(--paper); }
  .card--front .wordmark { top: 58px; font-size: 62px; color: var(--brand-green); }
  .card--front .wordmark__dot { background: var(--accent-blue); }

  .claims {
    position: absolute; top: 140px; left: 0; right: 0; text-align: center;
    font-size: 21px; line-height: 1.25;
  }
  .services { position: absolute; font-size: 19px; line-height: 1.45; list-style: none; }
  .services__item { padding-left: 20px; position: relative; }
  .services__item::before {
    content: ""; position: absolute; left: 2px; top: 9px;
    border-left: 8px solid var(--paper);
    border-top: 5px solid transparent; border-bottom: 5px solid transparent;
  }
  .services__title { font-weight: 700; }
  .services--winter { left: 62px; top: 196px; }
  .services--summer { left: 308px; top: 226px; }
  .services--extra { left: 530px; top: 253px; }

  .person { position: absolute; top: 212px; left: 155px; }
  .person__name { font-size: 28px; font-weight: 700; color: var(--brand-green); line-height: 1.3; }
  .person__title { font-size: 19px; color: var(--accent-blue); }
  .divider { position: absolute; left: 372px; top: 212px; width: 1px; height: 80px; background: var(--divider); }
  .phones { position: absolute; left: 390px; top: 214px; list-style: none; font-size: 21px; line-height: 1.6; }
  .phones__item { display: flex; align-items: center; gap: 10px; }
  .phones__icon { width: 18px; height: 18px; }
  .address { position: absolute; left: 150px; top: 306px; font-size: 20px; }

  .rule { position: absolute; left: 0; right: 0; height: 2px; background: var(--accent-blue); }
  .rule--upper { top: 342px; }
  .rule--lower { top: 390px; }
  .web-band {
    position: absolute; left: 0; right: 0; top: 348px; height: 36px;
    background: var(--brand-green); color: var(--paper);
    font-size: 20px; letter-spacing: 4px; padding-left: 150px; line-height: 36px;
  }
  .foot-band { position: absolute; left: 0; right: 0; top: 398px; height: 30px; background: var(--brand-green); }
</style>
</head>
<body>
  <section class="card card--back" aria-label="Card back">
    <div class="wordmark"><span class="wordmark__dot"></span>Brightfold</div>
    <p class="claims">Service Provider For Over 26 Years<br>Top 100 Snow Companies in the U.S.</p>
    <ul class="services services--winter">
      <li class="services__title">Winter Services</li>
      <li class="services__item">Snow Plowing</li>
      <li class="services__item">Sidewalk Clearing</li>
    </ul>
    <ul class="services services--summer">
      <li class="services__title">Summer Services</li>
      <li class="services__item">Mowing</li>
      <li class="services__item">Landscaping</li>
      <li class="services__item">Sodding</li>
    </ul>
    <ul class="services services--extra">
      <li class="services__item">Shrub Trimming</li>
      <li class="services__item">Clean-ups</li>
    </ul>
  </section>

  <section class="card card--front" aria-label="Card front">
    <div class="wordmark"><span class="wordmark__dot"></span>Brightfold</div>
    <div class="person">
      <p class="person__name">Your Name</p>
      <p class="person__title">Titlet</p>
    </div>
    <div class="divider"></div>
    <ul class="phones">
      <li class="phones__item">
        <svg class="phones__icon" viewBox="0 0 20 20" aria-hidden="true"><circle cx="10" cy="10" r="9" fill="none" stroke="#0f7a45" stroke-width="2"/><path d="M7 5c1 0 1.5 2 1 3l-1 1c.6 1.5 1.5 2.4 3 3l1-1c1-.5 3 0 3 1s-1 2-2.5 2C8 14 6 11 6 7.5 6 6 6.5 5 7 5z" fill="#0f7a45"/></svg>
        (417) 803-2765
      </li>
      <li class="phones__item">
        <svg class="phones__icon" viewBox="0 0 20 20" aria-hidden="true"><rect x="5" y="1" width="10" height="18" rx="2" fill="#0f7a45"/><rect x="7" y="4" width="6" height="9" fill="#ffffff"/></svg>
        (417) 803-5518
      </li>
    </ul>
    <p class="address">1879 Marigold, Larkmont OH 43917</p>
    <div class="rule rule--upper"></div>
    <div class="web-band">www.brightfold.com</div>
    <div class="rule rule--lower"></div>
    <div class="foot-band"></div>
  </section>
</body>
</html>
```